Industrial CNC laser cutting machine manufacturer needs a website designed

We need a website design for our company that re manufactures CNC laser cutting machines, we take old retired machines and completely re manufacture them from the ground up bringing them into the latest technology with all new parts and give them a new lease on life for a fraction of the cost of a new machine.

Machines can be fully customized to suit customers requirements too

My logo will need to be integrated and I want the website to look clean and modern

I will probably want 4 pages,Home, pictures, machines for sale and contact

Coding

Coded - Design and coding required

Number of Pages Required

1 page

```html
<!DOCTYPE html>
<html lang="en">
<head>
<meta charset="utf-8">
<title>Ridgeway Laser Rebuild</title>
<link href="https://fonts.googleapis.com/css2?family=Roboto+Condensed:wght@400;700&family=Ubuntu:wght@400;500&family=Roboto:wght@400;500;700&display=swap" rel="stylesheet">
<style>
:root{
  --red:#e0001b;
  --red-dark:#c40018;
  --ink:#1e1e1e;
  --text:#6b6b6b;
  --muted:#8a8a8a;
  --line:#d6d6d6;
  --grey-bg:#eef0f3;
  --grey-btn:#8c8c8c;
  --white:#ffffff;
}
*{box-sizing:border-box;margin:0;padding:0}
html,body{width:1200px;height:4016px;overflow:hidden;background:var(--white)}
body{position:relative;font-family:"Roboto",sans-serif;color:var(--ink)}
.abs{position:absolute}
.backdrop{position:absolute;left:0;top:0;width:1200px;height:4016px}

/* header */
.top-rule{left:0;top:0;width:1200px;height:3px;background:var(--red)}
.brand{left:86px;top:34px;display:flex;align-items:center;gap:12px}
.brand-mark{width:26px;height:26px;background:var(--red)}
.brand-name{font-family:"Roboto",sans-serif;font-weight:700;font-size:20px;letter-spacing:3px;color:#555;line-height:1.05;text-transform:uppercase}
.nav{left:468px;top:56px;display:flex;gap:0;font-family:"Roboto",sans-serif;font-weight:500;font-size:13px;text-transform:uppercase}
.nav a{color:var(--ink);text-decoration:none;position:absolute;white-space:nowrap}
.nav a.active{color:var(--red)}
.btn{display:flex;align-items:center;justify-content:center;background:var(--red);color:var(--white);font-family:"Roboto",sans-serif;font-weight:700;font-size:13px;text-transform:uppercase;border-radius:3px;text-decoration:none}
.login{left:989px;top:45px;width:99px;height:41px}

/* hero */
.hero-photo{left:0;top:118px;width:1200px;height:694px;background:radial-gradient(ellipse at 58% 45%,#e9a441 0%,#8a5a2c 22%,#3a3d48 55%,#20232b 100%)}
.hero-panel{left:162px;top:335px;width:876px;height:273px;background:rgba(38,40,48,.72);text-align:center;color:var(--white)}
.hero-panel h1{font-family:"Roboto Condensed",sans-serif;font-weight:700;font-size:52px;margin-top:36px;letter-spacing:.5px}
.hero-panel p{font-family:"Roboto Condensed",sans-serif;font-weight:700;font-size:14px;line-height:25px;margin-top:12px}
.hero-cta{left:527px;top:519px;width:146px;height:47px}
.dots{left:570px;top:714px;display:flex;gap:6px}
.dots span{width:13px;height:13px;border-radius:50%;border:2px solid var(--white)}
.dots span.on{background:var(--red);border-color:var(--red)}

/* about */
.about-frame{left:93px;top:888px;width:460px;height:429px;background:var(--red)}
.about-photo{left:111px;top:908px;width:459px;height:429px;background:linear-gradient(160deg,#5a6470 0%,#8d7f77 45%,#d9743f 75%,#f3c07a 100%)}
.eyebrow{left:633px;top:900px;font-family:"Ubuntu",sans-serif;font-weight:500;font-size:16px;letter-spacing:5px;color:var(--red)}
.about-title{left:631px;top:924px;font-family:"Ubuntu",sans-serif;font-weight:500;font-size:37px;color:var(--ink)}
.about-copy{left:633px;top:987px;width:450px;font-size:13px;line-height:25.7px;color:var(--text)}
.about-copy p+p{margin-top:25px}
.about-cta{left:633px;top:1287px;width:148px;height:47px}

.arrow-ico{display:inline-block;width:12px;height:12px;margin-left:4px;vertical-align:-1px}

/* section headings */
.section-title{left:0;width:1200px;text-align:center;font-family:"Roboto Condensed",sans-serif;font-weight:700;font-size:38px;color:var(--ink)}

/* machines */
.machine-card{width:312px;height:274px;background:var(--white);border:1px solid #cfd2d6;border-radius:3px;padding:22px}
.machine-shot{width:100%;height:100%;background:radial-gradient(ellipse at center,#d4d9df 0%,#eef1f4 60%,#fff 100%)}
.machine-name{width:312px;text-align:center;font-family:"Roboto",sans-serif;font-weight:500;font-size:20px;color:var(--ink)}
.machine-desc{width:312px;text-align:center;font-size:13px;line-height:25px;color:var(--muted)}
.machine-cta{width:148px;height:45px}
.slider-arrow{width:50px;height:50px;border-radius:50%;display:flex;align-items:center;justify-content:center}
.slider-arrow.prev{left:31px;top:1742px;background:#8e8e8e}
.slider-arrow.next{left:1121px;top:1742px;background:#2b2b2b}

/* pictures */
.gallery-tile{border-radius:2px}

/* testimonials */
.quotes-title{color:var(--white)}
.quote-card{width:311px;height:184px;background:var(--white);border-radius:8px;border:3px solid #f0b9c0;text-align:center;padding:68px 22px 0;font-size:13px;line-height:26px;color:#3a3a3a}
.quote-card::after{content:"";position:absolute;left:146px;bottom:-12px;border-left:10px solid transparent;border-right:10px solid transparent;border-top:12px solid var(--white)}
.avatar{width:94px;height:94px;border-radius:50%;border:4px solid var(--white);background:linear-gradient(180deg,#c9c2bb,#7d8792)}
.quote-name{width:311px;text-align:center;color:var(--white);font-weight:700;font-size:14px}
.quote-name small{font-weight:400;font-size:9px}
.stars{width:311px;text-align:center;color:#ffd400;font-size:13px;letter-spacing:1px}
.quotes-cta{left:506px;top:3353px;width:187px;height:50px;background:var(--grey-btn);font-size:13px}

/* footer */
.foot-title{font-family:"Roboto",sans-serif;font-weight:500;font-size:20px;color:var(--ink);text-transform:uppercase}
.foot-copy{font-size:14px;color:var(--text)}
.field{width:219px;height:42px;border:1px solid #bdbdbd;font-size:12px;color:#777;padding:13px 14px}
.submit{left:120px;top:3806px;width:453px;height:52px;font-size:18px;border-radius:0}
.contact-item{left:651px;display:flex;gap:12px;font-size:14px;line-height:22px;color:var(--text)}
.contact-item svg{flex:none;margin-top:3px}
.quick-links{left:958px;top:3645px;list-style:none;font-size:14px;line-height:29.5px;color:var(--text)}
.foot-rule{left:0;top:3894px;width:1200px;height:1px;background:#e5e5e5}
.legal{left:0;top:3943px;width:1200px;text-align:center;font-size:13px;color:#333}
</style>
</head>
<body>

<svg class="backdrop" viewBox="0 0 1200 4016" aria-hidden="true">
  <!-- machines band -->
  <polygon points="0,1514 600,1430 1200,1505 1200,2080 600,2160 0,2080" fill="#eceef1"/>
  <polygon points="0,1496 600,1430 600,1440 0,1515" fill="#e0001b"/>
  <polygon points="600,2160 1200,2078 1200,2096 600,2162" fill="#e0001b"/>
  <!-- testimonials band -->
  <polygon points="0,2938 600,2856 1200,2938 1200,3420 600,3498 0,3420" fill="#e0001b"/>
  <polygon points="0,2926 600,2852 600,2860 0,2940" fill="#8a8a8a"/>
  <polygon points="600,3498 1200,3410 1200,3424 600,3504" fill="#8a8a8a"/>
</svg>

<header>
  <div class="abs top-rule"></div>
  <div class="abs brand">
    <span class="brand-mark"></span>
    <span class="brand-name">Ridgeway<br>Laser Rebuild</span>
  </div>
  <nav class="abs nav">
    <a class="active" style="left:0">Home</a>
    <a style="left:80px">Pictures</a>
    <a style="left:182px">Machines for sale</a>
    <a style="left:355px">About</a>
    <a style="left:438px">Contact</a>
  </nav>
  <a class="abs btn login">Log in</a>
</header>

<section class="hero">
  <div class="abs hero-photo" role="img" aria-label="Laser cutting head throwing bright sparks across a metal sheet"></div>
  <svg class="abs" style="left:0;top:700px" width="1200" height="115" viewBox="0 700 1200 115" aria-hidden="true">
    <polygon points="0,735 600,812 1200,768 1200,815 0,815" fill="#fff"/>
    <polygon points="590,808 1200,738 1200,766 605,812" fill="#e0001b"/>
  </svg>
  <div class="abs hero-panel">
    <h1>RIDGEWAY LASER REBUILD</h1>
    <p>Lorem ipsum dolor sit amet, consectetur adipiscing elit, sed do eiusmod tempor incididunt ut labore et dolore magna aliqua.<br>Ut enim ad minim veniam, quis nostrud exercitation</p>
  </div>
  <a class="abs btn hero-cta">Get started</a>
  <div class="abs dots"><span class="on"></span><span></span><span></span></div>
</section>

<section class="about">
  <div class="abs about-frame"></div>
  <div class="abs about-photo" role="img" aria-label="Close-up of a laser cutting machine head with sparks"></div>
  <div class="abs eyebrow">ABOUT</div>
  <h2 class="abs about-title">Ridgeway Laser Rebuild</h2>
  <div class="abs about-copy">
    <p>Lorem ipsum dolor sit amet, consectetur adipiscing elit, sed do eiusmod tempor incididunt ut labore et dolore magna aliqua. Ut enim ad minim veniam, quis nostrud exercitation ullamco laboris nisi ut aliquip ex ea commodo consequat. Duis aute irure dolor in reprehenderit in voluptate velit esse cillum dolore eu fugiat nulla pariatur. Excepteur sint occaecat cupidatat non proident, sunt in culpa qui officia deserunt mollit anim id est laborum.</p>
    <p>Lorem ipsum dolor sit amet, consectetur adipiscing elit, sed do eiusmod tempor incididunt ut labore et dolore magna aliqua. Ut enim ad minim veniam, quis nostrud exercitation ullamco</p>
  </div>
  <a class="abs btn about-cta">Learn more <svg class="arrow-ico" viewBox="0 0 12 12"><circle cx="6" cy="6" r="6" fill="#fff"/><path d="M5 3l3 3-3 3" stroke="#e0001b" stroke-width="1.8" fill="none"/></svg></a>
</section>

<section class="machines">
  <h2 class="abs section-title" style="top:1518px">MACHINES FOR SALE</h2>

  <div class="abs slider-arrow prev"><svg width="18" height="18" viewBox="0 0 18 18"><path d="M11 3L5 9l6 6" stroke="#fff" stroke-width="2.4" fill="none"/></svg></div>
  <div class="abs slider-arrow next"><svg width="18" height="18" viewBox="0 0 18 18"><path d="M7 3l6 6-6 6" stroke="#fff" stroke-width="2.4" fill="none"/></svg></div>

  <div class="abs machine-card" style="left:111px;top:1589px"><div class="machine-shot" role="img" aria-label="Grey CNC lathe"></div></div>
  <div class="abs machine-card" style="left:444px;top:1589px"><div class="machine-shot" role="img" aria-label="Blue manual lathe"></div></div>
  <div class="abs machine-card" style="left:777px;top:1589px"><div class="machine-shot" role="img" aria-label="Enclosed vertical machining centre"></div></div>

  <div class="abs machine-name" style="left:111px;top:1882px">Lorem ipsum dolor</div>
  <div class="abs machine-name" style="left:444px;top:1882px">Lorem ipsum dolor</div>
  <div class="abs machine-name" style="left:777px;top:1882px">Lorem ipsum dolor</div>

  <div class="abs machine-desc" style="left:111px;top:1915px">Lorem ipsum dolor sit amet, consectetur<br>adipis cing elit, sed do eiusm</div>
  <div class="abs machine-desc" style="left:444px;top:1915px">Lorem ipsum dolor sit amet, consectetur<br>adipis cing elit, sed do eiusm</div>
  <div class="abs machine-desc" style="left:777px;top:1915px">Lorem ipsum dolor sit amet, consectetur<br>adipis cing elit, sed do eiusm</div>

  <a class="abs btn machine-cta" style="left:193px;top:1982px">Learn more <svg class="arrow-ico" viewBox="0 0 12 12"><circle cx="6" cy="6" r="6" fill="#fff"/><path d="M5 3l3 3-3 3" stroke="#e0001b" stroke-width="1.8" fill="none"/></svg></a>
  <a class="abs btn machine-cta" style="left:526px;top:1982px">Learn more <svg class="arrow-ico" viewBox="0 0 12 12"><circle cx="6" cy="6" r="6" fill="#fff"/><path d="M5 3l3 3-3 3" stroke="#e0001b" stroke-width="1.8" fill="none"/></svg></a>
  <a class="abs btn machine-cta" style="left:860px;top:1982px">Learn more <svg class="arrow-ico" viewBox="0 0 12 12"><circle cx="6" cy="6" r="6" fill="#fff"/><path d="M5 3l3 3-3 3" stroke="#e0001b" stroke-width="1.8" fill="none"/></svg></a>
</section>

<section class="pictures">
  <h2 class="abs section-title" style="top:2244px">OUR PICTURES</h2>
  <div class="abs gallery-tile" style="left:111px;top:2315px;width:314px;height:446px;background:linear-gradient(135deg,#e8ecef,#8f979f 55%,#3d434a)" role="img" aria-label="Drill bits and annular cutter"></div>
  <div class="abs gallery-tile" style="left:442px;top:2315px;width:315px;height:212px;background:linear-gradient(135deg,#c6ccd2,#6f7780 60%,#2f343a)" role="img" aria-label="Caliper measuring a machined part"></div>
  <div class="abs gallery-tile" style="left:442px;top:2549px;width:315px;height:212px;background:radial-gradient(ellipse at 50% 60%,#5d7180,#1c2630 60%,#3d6a1c 100%)" role="img" aria-label="Laser cutting a metal tube"></div>
  <div class="abs gallery-tile" style="left:774px;top:2315px;width:314px;height:446px;background:linear-gradient(160deg,#f3e6d2,#b9a187 45%,#6c6258 100%)" role="img" aria-label="Lathe chuck on a milling table"></div>
</section>

<section class="testimonials">
  <h2 class="abs section-title quotes-title" style="top:2938px">WHAT OUR CLIENT SAYS</h2>

  <div class="abs quote-card" style="left:111px;top:3072px">Sed ut perspiciatis unde omnis iste natus error sit voluptatem accusantium doloremque laudantium, totam rem aperiam, eaque ipsa quae ab illo</div>
  <div class="abs quote-card" style="left:444px;top:3072px">Sed ut perspiciatis unde omnis iste natus error sit voluptatem accusantium doloremque laudantium, totam rem aperiam, eaque ipsa quae ab illo</div>
  <div class="abs quote-card" style="left:777px;top:3072px">Lorem ipsum dolor sit consectetur adipiscing elit, sed do eiusmod tempor incididunt ut labore et dolore magna aliqua. Ut enim ad minim veniam,</div>

  <div class="abs avatar" style="left:219px;top:3022px" role="img" aria-label="Portrait of Dana Whitfield"></div>
  <div class="abs avatar" style="left:552px;top:3022px" role="img" aria-label="Portrait of Lena Park"></div>
  <div class="abs avatar" style="left:885px;top:3022px" role="img" aria-label="Portrait of Owen Marsh"></div>

  <div class="abs quote-name" style="left:111px;top:3283px">Dana Whitfield, <small>Chairman RLR</small></div>
  <div class="abs quote-name" style="left:444px;top:3283px">Lena Park, <small>Project Manager</small></div>
  <div class="abs quote-name" style="left:777px;top:3283px">Owen Marsh, <small>Chairman RLR</small></div>

  <div class="abs stars" style="left:111px;top:3305px">★★★★★</div>
  <div class="abs stars" style="left:444px;top:3305px">★★★★★</div>
  <div class="abs stars" style="left:777px;top:3305px">★★★★★</div>

  <a class="abs btn quotes-cta">View testimonials</a>
</section>

<footer>
  <h3 class="abs foot-title" style="left:120px;top:3595px">Ridgeway Laser Rebuild</h3>
  <p class="abs foot-copy" style="left:117px;top:3643px">Lorem ipsum dolor sit amet, consectetur adipiscing elit</p>
  <div class="abs field" style="left:120px;top:3683px">Name</div>
  <div class="abs field" style="left:355px;top:3683px">E - Mail</div>
  <div class="abs field" style="left:120px;top:3742px">Subject</div>
  <div class="abs field" style="left:355px;top:3742px">Message</div>
  <a class="abs btn submit">SUBMIT</a>

  <h3 class="abs foot-title" style="left:651px;top:3589px">Contact us</h3>
  <div class="abs contact-item" style="top:3645px">
    <svg width="16" height="18" viewBox="0 0 16 18"><path d="M8 1a6 6 0 0 0-6 6c0 4.5 6 10 6 10s6-5.5 6-10a6 6 0 0 0-6-6z" fill="none" stroke="#333" stroke-width="1.5"/><circle cx="8" cy="7" r="2" fill="none" stroke="#333" stroke-width="1.5"/></svg>
    <span>123,Lorem ipsum dolor sit amet,<br>consectetur adipiscing elit,<br>sed do eiusmod tempor</span>
  </div>
  <div class="abs contact-item" style="top:3728px">
    <svg width="16" height="16" viewBox="0 0 16 16"><path d="M3 1l3 3-1.5 2a9 9 0 0 0 5.5 5.5L12 10l3 3-2 2C7 15 1 9 1 3z" fill="none" stroke="#333" stroke-width="1.4"/></svg>
    <span>Phone: +1 888 888 8888</span>
  </div>
  <div class="abs contact-item" style="top:3776px">
    <svg width="16" height="16" viewBox="0 0 16 16"><circle cx="8" cy="8" r="6.5" fill="none" stroke="#333" stroke-width="1.5"/><path d="M8 4v4h3" stroke="#333" stroke-width="1.5" fill="none"/></svg>
    <span>Time : Mon-fri 8am-5pm Mst</span>
  </div>
  <div class="abs contact-item" style="top:3827px">
    <svg width="17" height="14" viewBox="0 0 17 14"><rect x="1" y="1" width="15" height="12" fill="none" stroke="#333" stroke-width="1.4"/><path d="M1 1l7.5 6L16 1" fill="none" stroke="#333" stroke-width="1.4"/></svg>
    <span>Email: info@companyname.com</span>
  </div>

  <h3 class="abs foot-title" style="left:958px;top:3589px">Quick links</h3>
  <ul class="abs quick-links">
    <li>Home</li><li>About Us</li><li>Pictures</li><li>Machines for sale</li><li>Reviews</li><li>Contact Us</li>
  </ul>

  <div class="abs foot-rule"></div>
  <p class="abs legal">(c) 2020 Company name | All Rights Reserved | Terms and Conditions</p>
</footer>

</body>
</html>
```